Presentation Brochure and Sample Box Design for Veto Sheet

Veto Sheet is a colour coated solid aluminium panel that our company supplies to the signage and building cladding industries.
We require an, A4 double-sided folding brochure (swatch book) that folds 3 ways, opening once and then a second time to lay out 3 pages flat.

There should be a front and back cover.

The inside cover should be reserved with text blocks for written information about the panel.

The opposite page on the right when you first open the brochure should have all our Matte PVDF 2mm colours which you will find in the attached PDF of colour swatches and details.

When the brochure is folded out a second time, showing all three inside pages flat, the two inside pages on the right (next to the inside cover with the written information) should show all our FEVE Gloss 1.6mm colours which you will also find in the attached PDF colour book.

This brochure should have a modern and professional feel suitable for presenting to architects and designers.

We also require a box design to contain aluminium samples of all the colours in the range.

Please refer to the template attached for the box dimensions and layout.

The box should tie in with the brochure as a complete package with a modern and professional look suitable for presenting to architects and designers.

Finally we require a small label sticker to be stuck on the back of each sample. On the sticker should be the Veto Sheet logo, a space to put the product code for the sample colour and the phone number 1300 584 396.

To summarise, this package project includes:
1 tri-folding A4 brochure,
1 sample box package design,
1 sample sticker label.

This is our signature new product that we will be marketing to signage installers to create coloured and printed aluminium signs. We are also looking to move further into the building and architectural market place with this product.

Please refer to the attachments for the Veto Sheet logo - the colour swatch book and template for the sample box.
The Veto Sheet logo can be shown in White, Black or Silver.

Target Market(s)

Architects, interior designers, builders and signage installers.

Font styles to use
Serif
Sans Serif

Requirements
Must have
• A modern, neat and professional upmarket look suitable for presenting to architects.
Nice to have
• A slick and classy look that makes you want to take home the box or brochure even if you're not interested in the product.
Should not have
• A cheap, untidy, low market look with too many colours.

```html
<!DOCTYPE html>
<html lang="en">
<head>
<meta charset="utf-8">
<title>Veto Sheet – Label Sticker</title>
<link rel="stylesheet" href="https://fonts.googleapis.com/css2?family=Archivo+Black&family=Montserrat:wght@600;700&display=swap">
<style>
  :root {
    --page-bg: #ededed;
    --ink: #161616;
    --ring-text: #1c1c1c;
    --star-dark: #2e2c36;
    --star-light: #8c8c8e;
    --red: #d41f30;
    --red-edge: #6e0c16;
    --yellow: #f2ea24;
    --yellow-edge: #6f6608;
    --blue: #1d87c4;
    --blue-edge: #0a3350;
    --navy: #25347a;
    --navy-edge: #0b1030;
    --logo-white: #ffffff;
  }
  html, body {
    margin: 0;
    padding: 0;
    width: 1200px;
    height: 1200px;
    overflow: hidden;
    background: var(--page-bg);
  }
  .sheet {
    position: relative;
    width: 1200px;
    height: 1200px;
  }
  .sheet-title {
    position: absolute;
    top: 64px;
    left: 0;
    width: 1200px;
    margin: 0;
    text-align: center;
    font-family: "Montserrat", sans-serif;
    font-weight: 700;
    font-size: 38px;
    letter-spacing: 1px;
    color: var(--ink);
  }
  .sticker-sheet {
    position: absolute;
    top: 0;
    left: 0;
  }
  .ring-text {
    font-family: "Archivo Black", sans-serif;
    font-size: 35px;
    fill: var(--ring-text);
  }
  .brand-name {
    font-family: "Montserrat", sans-serif;
    font-weight: 600;
    font-size: 29px;
    letter-spacing: 2px;
    fill: var(--logo-white);
  }
  .disc-red { --disc: var(--red); --disc-edge: var(--red-edge); }
  .disc-yellow { --disc: var(--yellow); --disc-edge: var(--yellow-edge); }
  .disc-blue { --disc: var(--blue); --disc-edge: var(--blue-edge); }
  .disc-navy { --disc: var(--navy); --disc-edge: var(--navy-edge); }
  .disc-edge { fill: var(--disc-edge); }
  .disc-face { fill: var(--disc); }
</style>
</head>
<body>
<main class="sheet">
  <h1 class="sheet-title">LABEL STICKER</h1>

  <svg class="sticker-sheet" width="1200" height="1200" viewBox="0 0 1200 1200">
    <defs>
      <linearGradient id="metal" x1="0" y1="0" x2="1" y2="1">
        <stop offset="0" stop-color="#d9d9dc"/>
        <stop offset="0.18" stop-color="#8b8b8f"/>
        <stop offset="0.32" stop-color="#f4f4f6"/>
        <stop offset="0.5" stop-color="#9a9aa0"/>
        <stop offset="0.62" stop-color="#4b4a58"/>
        <stop offset="0.75" stop-color="#c8c8cc"/>
        <stop offset="0.88" stop-color="#f6f6f8"/>
        <stop offset="1" stop-color="#6f6e7a"/>
      </linearGradient>
      <linearGradient id="metal-rim" x1="1" y1="0" x2="0" y2="1">
        <stop offset="0" stop-color="#6a6a72"/>
        <stop offset="0.5" stop-color="#ffffff"/>
        <stop offset="1" stop-color="#54535e"/>
      </linearGradient>
      <path id="arc-top" d="M -181,-28 A 183 183 0 0 1 181,-28"/>
      <path id="arc-bottom" d="M -172,122 A 211 211 0 0 0 172,122"/>
      <polygon id="star" points="0,-19 4.5,-6 18,-6 7,2.5 11,16 0,8 -11,16 -7,2.5 -18,-6 -4.5,-6"/>

      <g id="sticker-ring">
        <circle r="234" fill="url(#metal)"/>
        <circle r="225" fill="none" stroke="url(#metal-rim)" stroke-width="1.6"/>
        <circle r="217" fill="none" stroke="#ffffff" stroke-opacity="0.5" stroke-width="0.8"/>
        <text class="ring-text">
          <textPath href="#arc-top" startOffset="50%" text-anchor="middle" textLength="500" lengthAdjust="spacing">CALL US! 1300-584-396</textPath>
        </text>
        <text class="ring-text">
          <textPath href="#arc-bottom" startOffset="50%" text-anchor="middle" textLength="350" lengthAdjust="spacing">PRODUCT CODE</textPath>
        </text>
        <use href="#star" x="-177" y="39" fill="var(--star-dark)"/>
        <use href="#star" x="182" y="39" fill="var(--star-light)"/>
      </g>

      <g id="sticker-face">
        <circle class="disc-edge" r="150"/>
        <circle class="disc-face" r="143"/>
        <circle r="136" fill="none" stroke="#ffffff" stroke-opacity="0.75" stroke-width="0.9"/>
        <text class="brand-name" x="0" y="11" text-anchor="middle">VETO SHEET</text>
      </g>
    </defs>

    <g class="sticker disc-red" transform="translate(331 401)">
      <use href="#sticker-ring"/>
      <use href="#sticker-face"/>
    </g>
    <g class="sticker disc-yellow" transform="translate(869 401)">
      <use href="#sticker-ring"/>
      <use href="#sticker-face"/>
    </g>
    <g class="sticker disc-blue" transform="translate(331 902)">
      <use href="#sticker-ring"/>
      <use href="#sticker-face"/>
    </g>
    <g class="sticker disc-navy" transform="translate(869 902)">
      <use href="#sticker-ring"/>
      <use href="#sticker-face"/>
    </g>
  </svg>
</main>
</body>
</html>
```